Create Awesome Sale/AD graphics for BLACK FRIDAY

Create a (3) Black Friday graphics integrating our supplied pictures .
Text requirements = Black Friday/Cyber Monday sale
Text requirements = Deals up to 50% off
Text requirements = www.BLUMORAK.co
Integrate Blu Morak Logo

We would like to drop these graphics into a video, and use for Social Medai post's we would like perimeter around the graphic to be dark to fit the theme the graphic will be added at @15-17 sec in this video:
Youtube Video this Ad is live for this request here:
https://www.vidplexa.com/watch?v=ZqT4mLw8RbE

I will upload a series of images we would like to use, choose the three you like to use.

Typically when we have graphics generated we get a zip file of the graphics in these formats EPS/AI/PDF/JPEG/PNG

Target Market(s)

Fishing, 50% mix male/female, ages 18-35

Colors

Designer to choose colors to be used in the design.

Requirements
Must have
• Create a (3) Black Friday graphics integrating our supplied pictures .
• Text requirements = Black Friday/Cyber Monday sale
• Text requirements = Deals up to 50% off
• Text requirements = www.BLUMORAK.co
• Integrate Blu Morak Logo
• ** I have more Blu Morak EPS/AI if needed See attached
Nice to have
• We would like to drop these graphics into a video, and use for Social Medai post's we would like perimeter around the graphic to be dark tto fit the theme the graphic will be added at @15-17 sec in this video:
• Youtube Video this Ad is live for this request here:
• https://www.vidplexa.com/watch?v=ZqT4mLw8RbE
Should not have
• a lot of white space

```html
<!DOCTYPE html>
<html lang="en">
<head>
<meta charset="utf-8">
<title>Blu Morak Black Friday Cyber Monday Sale Graphics</title>
<link href="https://fonts.googleapis.com/css2?family=Open+Sans:wght@400;700;800&family=Yellowtail&display=swap" rel="stylesheet">
<style>
  :root {
    --ink: #0b0b0c;
    --gold: #fbbd0f;
    --white: #ffffff;
    --paper: #ffffff;
    --logo-grey: #9a9a9a;
  }
  * { margin: 0; padding: 0; box-sizing: border-box; }
  html, body { width: 1200px; height: 969px; overflow: hidden; background: var(--paper); }
  body { position: relative; font-family: "Open Sans", Arial, sans-serif; }

  .ad { position: absolute; background: var(--ink); overflow: hidden; box-shadow: 0 10px 10px -6px rgba(0,0,0,0.35); }
  .ad > * { position: absolute; }
  .photo { display: block; }

  .script { font-family: "Yellowtail", cursive; color: var(--white); line-height: 1; white-space: nowrap; }
  .band { background: var(--gold); color: var(--ink); font-weight: 700; line-height: 1; display: flex; align-items: center; justify-content: center; white-space: nowrap; }
  .sale { color: var(--white); font-weight: 800; line-height: 1; letter-spacing: 1px; }

  .badge { border-radius: 50%; background: var(--ink); border: 2px solid var(--gold); color: var(--white); text-align: center; }
  .badge .lead { display: block; font-size: 9px; transform: rotate(8deg); }
  .badge .big { color: var(--gold); font-weight: 800; }
  .badge .pct { font-weight: 800; font-size: 0.55em; color: var(--white); }

  .brand { font-weight: 700; white-space: nowrap; display: flex; align-items: center; gap: 5px; }
  .brand .dot { width: 8px; height: 8px; border-radius: 50%; background: currentColor; }

  /* Panel one */
  .ad-one { left: 47px; top: 305px; width: 356px; height: 360px; }
  .ad-one .photo { left: 0; top: 0; width: 356px; height: 182px; background: linear-gradient(160deg, #3f5a33 0%, #5d6f4d 45%, #6f7f8a 75%, #4a5a60 100%); }
  .ad-one .frame { left: 24px; top: 25px; width: 308px; height: 311px; border: 1.5px solid var(--gold); }
  .ad-one .brand { left: 34px; top: 46px; color: var(--white); font-size: 11px; }
  .ad-one .badge { left: 230px; top: 12px; width: 104px; height: 104px; padding-top: 26px; }
  .ad-one .badge .big { font-size: 34px; line-height: 1; }
  .ad-one .script { left: 0; width: 356px; top: 190px; text-align: center; font-size: 36px; }
  .ad-one .band { left: 87px; top: 227px; width: 188px; height: 24px; font-size: 20px; }
  .ad-one .sale { left: 0; width: 356px; top: 250px; text-align: center; font-size: 62px; }
  .ad-one .url { left: 105px; top: 321px; width: 146px; height: 32px; border-radius: 16px; background: var(--gold); color: var(--ink); font-size: 11px; display: flex; align-items: center; justify-content: center; }

  /* Panel two */
  .ad-two { left: 418px; top: 305px; width: 357px; height: 360px; }
  .ad-two .photo { left: 50px; top: 14px; width: 292px; height: 320px; background: linear-gradient(135deg, #8c8a76 0%, #a7a38f 30%, #c9a892 60%, #b7b3ad 100%); clip-path: polygon(0 0, 100% 0, 100% 100%, 27.5% 100%); }
  .ad-two .script { left: 22px; top: 80px; font-size: 34px; }
  .ad-two .band { left: 10px; top: 115px; width: 187px; height: 26px; font-size: 20px; }
  .ad-two .sale { left: 10px; top: 147px; font-size: 68px; }
  .ad-two .tag { left: 44px; top: 219px; width: 84px; height: 40px; background: var(--gold); transform: rotate(22deg); color: var(--ink); padding-left: 14px; clip-path: polygon(14% 0, 100% 0, 100% 100%, 14% 100%, 0 50%); }
  .ad-two .tag .lead { display: block; font-size: 8px; color: var(--white); line-height: 1; padding-top: 4px; }
  .ad-two .tag .big { font-size: 26px; font-weight: 800; line-height: 1; }
  .ad-two .tag .pct { font-size: 12px; font-weight: 800; }
  .ad-two .brand { left: 8px; top: 330px; color: var(--logo-grey); font-size: 14px; }
  .ad-two .url { left: 125px; top: 339px; color: var(--white); font-size: 12px; }

  /* Panel three */
  .ad-three { left: 787px; top: 303px; width: 361px; height: 365px; }
  .ad-three .photo { left: 0; top: 0; width: 361px; height: 194px; background: linear-gradient(180deg, #4d6a48 0%, #5c7550 22%, #8d9aa1 40%, #b3bcc1 70%, #9aa4a8 100%); }
  .ad-three .frame { left: 19px; top: 19px; width: 324px; height: 327px; border: 1px solid var(--white); }
  .ad-three .badge { left: 280px; top: 37px; width: 76px; height: 76px; padding-top: 18px; }
  .ad-three .badge .lead { font-size: 7px; }
  .ad-three .badge .big { font-size: 22px; line-height: 1; }
  .ad-three .script { left: 0; width: 366px; top: 198px; text-align: center; font-size: 44px; }
  .ad-three .band { left: 55px; top: 246px; width: 258px; height: 35px; font-size: 27px; }
  .ad-three .sale { left: 55px; top: 282px; font-size: 64px; }
  .ad-three .brand { left: 233px; top: 313px; color: var(--logo-grey); font-size: 11px; }
  .ad-three .url { left: 92px; top: 352px; width: 176px; height: 13px; background: var(--gold); color: var(--ink); font-size: 9px; font-weight: 700; display: flex; align-items: center; justify-content: center; }
</style>
</head>
<body>

<section class="ad ad-one">
  <div class="photo" role="img" aria-label="Angler in a cap holding a large rainbow trout beside a forest river"></div>
  <div class="frame"></div>
  <div class="brand"><span class="dot"></span>Blu Morak</div>
  <div class="badge"><span class="lead">DEALS UP TO</span><span class="big">50<span class="pct">%OFF</span></span></div>
  <div class="script">Black Friday</div>
  <div class="band">CYBER MONDAY</div>
  <div class="sale">SALE</div>
  <div class="url">www.BLUMORAK.co</div>
</section>

<section class="ad ad-two">
  <div class="photo" role="img" aria-label="Close-up of an angler wearing an embroidered trucker cap and blue sunglasses"></div>
  <div class="script">Black Friday</div>
  <div class="band">CYBER MONDAY</div>
  <div class="sale">SALE</div>
  <div class="tag"><span class="lead">DEALS UP TO</span><span class="big">50</span><span class="pct">%OFF</span></div>
  <div class="brand"><span class="dot"></span>Blu Morak</div>
  <div class="url">www.BLUMORAK.co</div>
</section>

<section class="ad ad-three">
  <div class="photo" role="img" aria-label="Angler in a cap crouching in a river holding a silver salmon"></div>
  <div class="frame"></div>
  <div class="badge"><span class="lead">DEALS UP TO</span><span class="big">50<span class="pct">%OFF</span></span></div>
  <div class="script">Black Friday</div>
  <div class="band">CYBER MONDAY</div>
  <div class="sale">SALE</div>
  <div class="brand"><span class="dot"></span>Blu Morak</div>
  <div class="url">www.BLUMORAK.co</div>
</section>

</body>
</html>
```